Online-Marketing Material für Beraternetzwerk
Zielgruppe
Ich habe ein Beraternetzwerk im deutschen Gesundheitswesen gegründet, gleichzeitig einen gemeinnützigen Verein, habe zwei webseiten www.kv-pflegeberatung-demo.de + www.kv-pflegefreunde-demo.de, Logo, Briefpapier etc. sind vorhanden. Hauptfarbe GmbH RGB 185/87/120 Hex#B95778, Verein RGB 226/125/119 Hex#E27D77. Die Organisationen sind grundsätzlich getrennt, aber es gibt eine Zusammenarbeit und Partner meines Netzwerkes sind auch Fördermitglieder im Verein
Aufgabenstellung
Die beiden Firmenfarben müssen verwendet werden, für die GmbH hauptsächlich die eigene, die 2. Farbe darf mit verwendet werden. Es darf insgesamt feminin wirken, aber nicht verspielt oder gar niedlich. Ich bin Business-Frau;-). Als Schrift habe ich mich auf Avenir next konzentriert, die Agentur hat auch Alternate Gothic auf den Webseiten verwendet. Jetzt benötige ich für eine Veranstaltungsreihe die Ausarbeitung von LinkedIn, Facebook/Insta, Einladung per Brevo und E-Mail Grafiken. Es sind immer Veranstaltungen, zu denen ich einlade und in denen meine Geschäftspartner ihre Expertise gegenüber Kunden darstellen. Die Veranstaltungen sind als Duo zu sehen 1. Präsenz in München, 2. als Online Meeting ein paar Tage später. Die Location wird das Hotel Marwin, direkt am Brunnenhofplatz in München sein. Start der Präsenzveranstaltung 11:00, anschließend Mittagessen. Als Titel für die Veranstaltungen sehe ich 'KlinikForum' vor, es wird jeweils noch ein inhaltliches Thema wie z.B. 'Unternehmenskauf/-verkauf' ergänzt. Erster Termin ist vss. am 15. September 2023. Anbei auch ein paar erste Entwürfe 'meiner' Agentur nebst Feedback von mir. Ich glaube inzwischen nicht, dass hier etwas vernünftiges produziert wird, deshalb mein Versuch auf diesem Weg. Weitere Zusammenarbeit dann herzlich gerne

```html
<!DOCTYPE html>
<html lang="de">
<head>
<meta charset="utf-8">
<title>KlinikForum – Einladung</title>
<link rel="stylesheet" href="https://fonts.googleapis.com/css2?family=Nunito+Sans:wght@200;300;400;600;700;800;900&display=swap">
<style>
  :root {
    --brand-gmbh: #b95778;
    --brand-verein: #e27d77;
    --bg-left: #c9577f;
    --bg-mid: #d47f86;
    --bg-right: #e6a58c;
    --band: #a2456a;
    --wall-light: #ece4db;
    --wall-warm: #d9c7b8;
    --text: #ffffff;
  }
  * { margin: 0; padding: 0; box-sizing: border-box; }
  html, body { width: 1200px; height: 630px; overflow: hidden; }
  body { font-family: "Nunito Sans", "Avenir Next", sans-serif; color: var(--text); }

  .event-card {
    position: relative;
    width: 1200px;
    height: 630px;
    overflow: hidden;
    background: linear-gradient(90deg, var(--bg-left) 0%, var(--bg-left) 18%, var(--bg-mid) 50%, var(--bg-right) 72%, var(--bg-right) 100%);
  }

  .speaker-photo {
    position: absolute;
    right: 0; top: 0;
    width: 470px; height: 630px;
    background:
      radial-gradient(ellipse 160px 300px at 62% 70%, rgba(70,72,80,0.55), rgba(70,72,80,0) 100%),
      linear-gradient(90deg, rgba(230,165,140,0) 0%, var(--wall-warm) 35%, var(--wall-light) 100%);
  }

  .headline {
    position: absolute;
    left: 38px; top: 22px;
    font-size: 118px;
    line-height: 1;
    letter-spacing: 1px;
    white-space: nowrap;
  }
  .headline .light { font-weight: 200; }
  .headline .bold { font-weight: 900; }

  .date-band { position: absolute; left: 40px; top: 200px; width: 234px; height: 346px; }
  .date {
    position: absolute;
    left: 40px; top: 250px; width: 232px;
    text-align: center;
    line-height: 1;
  }
  .date-day { font-size: 118px; font-weight: 900; letter-spacing: -2px; }
  .date-month { font-size: 46px; font-weight: 400; margin-top: 2px; }
  .date-year { font-size: 70px; font-weight: 900; margin-top: 2px; }

  .registration {
    position: absolute;
    left: 40px; top: 549px; width: 256px;
    text-align: center;
    font-size: 11px;
    line-height: 1.3;
  }
  .registration strong { font-weight: 800; }
  .registration-mail { display: block; font-size: 15px; margin-top: 16px; }

  .details {
    position: absolute;
    left: 330px; top: 152px; width: 450px;
    text-align: center;
    line-height: 1.1;
  }
  .topic { font-size: 40px; font-weight: 800; }
  .presented-by { font-size: 13px; font-weight: 400; margin-top: 10px; }
  .presenter { font-size: 20px; font-weight: 400; margin-top: 2px; }
  .venue { font-size: 22px; font-weight: 800; margin-top: 16px; }
  .venue-note { font-size: 10px; font-weight: 400; margin-top: 2px; }
  .format { font-size: 39px; font-weight: 900; margin-top: 14px; }
  .time { font-size: 70px; font-weight: 900; letter-spacing: 1px; line-height: 1; }

  .online-band { position: absolute; left: 318px; top: 440px; width: 460px; height: 66px; }
  .online {
    position: absolute;
    left: 330px; top: 446px; width: 440px;
    text-align: center;
    line-height: 1;
  }
  .online-date { font-size: 34px; font-weight: 400; }
  .online-url { font-size: 12px; font-weight: 800; margin-top: 6px; }

  .organizer {
    position: absolute;
    left: 410px; top: 540px;
    display: flex; align-items: center; gap: 14px;
  }
  .organizer-mark { width: 52px; height: 52px; border-radius: 50%; background: var(--text); opacity: 0.9; }
  .organizer-name { font-size: 24px; font-weight: 700; line-height: 1.1; }
</style>
</head>
<body>
<main class="event-card">
  <div class="speaker-photo" role="img" aria-label="Porträtfoto der Gastgeberin im dunklen Blazer vor heller Steinwand"></div>

  <h1 class="headline"><span class="light">KLINIK</span> <span class="bold">FORUM</span></h1>

  <svg class="date-band" viewBox="0 0 234 346" aria-hidden="true">
    <polygon points="0,0 234,46 234,346 0,306" fill="var(--band)"/>
  </svg>
  <div class="date">
    <div class="date-day">15.</div>
    <div class="date-month">September</div>
    <div class="date-year">2023</div>
  </div>

  <p class="registration">
    Begrenzte Teilnehmerzahl<br>
    <strong>Bitte anmelden unter:</strong>
    <span class="registration-mail">info@kv-pflegeberatung-demo.de</span>
  </p>

  <section class="details">
    <div class="topic">“tolles&nbsp; Thema”</div>
    <div class="presented-by">präsentiert von</div>
    <div class="presenter">Beispielsfirma</div>
    <div class="venue">im Hotel Marwin München</div>
    <div class="venue-note">direkt am Brunnenhofplatz</div>
    <div class="format">Präsenzveranstaltung</div>
    <div class="time">11:00 Uhr</div>
  </section>

  <svg class="online-band" viewBox="0 0 460 66" aria-hidden="true">
    <polygon points="28,0 460,0 432,66 0,66" fill="var(--band)"/>
  </svg>
  <div class="online">
    <div class="online-date">online am x.xx.23</div>
    <div class="online-url">www.kv-pflegeberatung-demo.de/online</div>
  </div>

  <div class="organizer">
    <span class="organizer-mark" aria-hidden="true"></span>
    <span class="organizer-name">KV Pflegeberatung<br>GmbH</span>
  </div>
</main>
</body>
</html>
```